Feedback App to request feedback from colleagues

It’s a small web app to collect feedback from team members. This is the general screen flow but happy for variations to it.

Users logs into application and is able to see the feedback received till date from different colleagues.

At the top right are “Request feedback”, “Respond to Feedback”.

When the user clicks on Request Feedback, there are three options.
Adhoc Feedback
Mid Year Feedback
360 Feedback

Adhoc feedback will open a screen where I can search for colleagues to request feedback from (I can select more than one). There are three pre-defined question that can I edit if needed.

Mid year feedback: same process but questions cannot be edited

360 Feedback - just redirect to another website.

Respond to Feedback - see incoming request and the ability to provide feedback to questions received.

Send Feedback: select a colleague and send adhoc feedback.

Colours to be used are white and red only. Simple design, the app will be embedded in a portal so need for headers etc. think of a mobile view but no need for logo, header bar etc

Colour Codes:
Red: #E60000
White #FFFFFF
Grey: #333333 (Only use if needed e.g. borders, background etc)
Black: #000000

Only the above colours to be used

Number of Pages Required

1 page

Font styles to use
Sans Serif

Colors
EB3D1F
EC4F4E
F09395
F8D3D4
FCEDEE

Requirements
Must have
• Design screens for every page mentioned
Nice to have
• Clean design, use of images and icons
Should not have
• Cluttered design, header

```html
<!DOCTYPE html>
<html lang="en">
<head>
<meta charset="utf-8">
<title>Feedback App</title>
<link href="https://fonts.googleapis.com/css2?family=Montserrat:wght@500&family=Roboto:wght@400;500;700&display=swap" rel="stylesheet">
<style>
  :root {
    --stage: #595959;
    --surface: #ffffff;
    --red: #ee3b1f;
    --ink: #222222;
    --muted: #555555;
    --soft: #8a8a8a;
    --line: #e6e6e6;
    --star: #f7a000;
    --card-border: #e4e4e4;
  }
  * { box-sizing: border-box; margin: 0; padding: 0; }
  html, body { width: 1200px; height: 2282px; overflow: hidden; }
  body { background: var(--stage); position: relative; font-family: 'Roboto', sans-serif; color: var(--ink); }

  .screen { position: absolute; left: 26px; width: 1148px; height: 717px; background: var(--surface); }
  .screen--home { top: 26px; }
  .screen--menu { top: 782px; }
  .screen--adhoc { top: 1537px; }

  .toolbar { position: absolute; left: 0; top: 0; width: 100%; height: 114px; border-bottom: 1px solid var(--line); }
  .btn { position: absolute; top: 33px; height: 51px; border-radius: 26px; font-weight: 700; font-size: 15px;
         display: flex; align-items: center; justify-content: center; }
  .btn--solid { left: 732px; width: 167px; background: var(--red); color: #fff; box-shadow: 0 4px 10px rgba(238,59,31,.3); }
  .btn--outline { left: 913px; width: 182px; border: 2px solid var(--red); color: var(--red); background: #fff; }

  .card { position: absolute; width: 283px; height: 120px; border: 1px solid var(--card-border); border-radius: 4px; background: #fff; padding: 16px 20px 0 21px; }
  .card--raised { box-shadow: 0 3px 8px rgba(0,0,0,.16); border-color: #ececec; }
  .card .stars { display: flex; gap: 3px; }
  .card .quote { font-family: 'Montserrat', sans-serif; font-weight: 500; font-size: 13.5px; line-height: 18px; margin-top: 10px; text-transform: uppercase; color: #111; }
  .card .author { position: absolute; right: 72px; bottom: 22px; font-size: 10px; color: var(--red); text-transform: uppercase; }
  .card .avatar { position: absolute; right: 11px; bottom: 10px; width: 44px; height: 44px; }
  .c1 { left: 105px; } .c2 { left: 431px; } .c3 { left: 759px; }
  .r1 { top: 229px; } .r2 { top: 394px; }

  .avatar { border-radius: 50%; background: radial-gradient(circle at 50% 40%, #d9b49a 0 30%, #6b4a3a 55%, #e9e6e2 80%); }
  .avatar--b { background: radial-gradient(circle at 50% 40%, #c99a78 0 30%, #4a3a30 55%, #cfc6b8 80%); }
  .avatar--c { background: radial-gradient(circle at 50% 45%, #e6c2a8 0 30%, #5a3c2e 58%, #d8d4d0 80%); }

  .menu { position: absolute; left: 742px; top: 86px; width: 154px; height: 115px; background: #fff; border-radius: 4px;
          box-shadow: 0 3px 12px rgba(0,0,0,.14); padding-top: 14px; }
  .menu li { list-style: none; font-size: 14px; color: #333; padding-left: 21px; height: 28.5px; line-height: 22px; }

  .title { position: absolute; top: 30px; width: 100%; text-align: center; font-size: 30px; font-weight: 700; color: #222; }
  .divider { position: absolute; top: 89px; left: 0; width: 100%; border-top: 1px solid var(--line); }
  .search { position: absolute; left: 105px; top: 104px; width: 290px; height: 49px; border-radius: 25px; background: #fff;
            box-shadow: 0 2px 10px rgba(0,0,0,.12); display: flex; align-items: center; justify-content: space-between; padding: 0 4px 0 22px;
            font-size: 13px; color: #666; }
  .search .go { width: 40px; height: 40px; border-radius: 50%; background: var(--red); display: flex; align-items: center; justify-content: center; }

  .row { position: absolute; left: 107px; width: 934px; height: 79px; background: #fff; border-radius: 6px; box-shadow: 0 2px 10px rgba(0,0,0,.07); }
  .row .avatar { position: absolute; left: 28px; top: 25px; width: 30px; height: 30px; }
  .row .name { position: absolute; left: 75px; top: 31px; font-size: 14px; color: #333; }
  .row .meta { position: absolute; left: 243px; top: 22px; font-size: 11px; color: var(--soft); }
  .row .meta .stars { display: flex; gap: 4px; margin-top: 6px; }
  .row .action { position: absolute; right: 31px; top: 28px; font-size: 15px; font-weight: 500; color: var(--red); }
  .row--open { height: 124px; }
  .row--open .action { right: 63px; }
  .row .edit { position: absolute; right: 23px; top: 30px; }
  .questions { position: absolute; left: 394px; top: 22px; list-style: none; }
  .questions li { display: flex; align-items: center; gap: 7px; font-size: 11.5px; color: #666; height: 31.5px; margin-top: -9px; }
</style>
</head>
<body>
<svg width="0" height="0" style="position:absolute">
  <defs>
    <symbol id="star" viewBox="0 0 24 24"><path fill="#f7a000" d="M12 2l2.9 6.6 7.1.6-5.4 4.7 1.6 7L12 17.3 5.8 21l1.6-7L2 9.2l7.1-.6z"/></symbol>
    <symbol id="stars" viewBox="0 0 76 12">
      <use href="#star" x="0" width="12" height="12"/><use href="#star" x="16" width="12" height="12"/>
      <use href="#star" x="32" width="12" height="12"/><use href="#star" x="48" width="12" height="12"/>
      <use href="#star" x="64" width="12" height="12"/>
    </symbol>
    <symbol id="tick" viewBox="0 0 12 12"><circle cx="6" cy="6" r="6" fill="#333"/><path d="M3.3 6.2l1.8 1.8 3.6-3.6" stroke="#fff" stroke-width="1.5" fill="none"/></symbol>
  </defs>
</svg>

<!-- Home: feedback received -->
<section class="screen screen--home">
  <div class="toolbar">
    <div class="btn btn--solid">Request feedback</div>
    <div class="btn btn--outline">Respond to Feedback</div>
  </div>
  <article class="card c1 r1"><svg class="stars" width="72" height="12"><use href="#stars"/></svg><p class="quote">Lorem ipsum dolor sit ipimetc onsectetur adipiscing</p><span class="author">Mark Ellis</span><div class="avatar" role="img" aria-label="Portrait of Mark Ellis"></div></article>
  <article class="card card--raised c2 r1"><svg class="stars" width="72" height="12"><use href="#stars"/></svg><p class="quote">Lorem ipsum dolor sit ipimetc onsectetur adipiscing</p><span class="author">Leo</span><div class="avatar avatar--b" role="img" aria-label="Portrait of Leo"></div></article>
  <article class="card c3 r1"><svg class="stars" width="72" height="12"><use href="#stars"/></svg><p class="quote">Lorem ipsum dolor sit ipimetc onsectetur adipiscing</p><span class="author">Renata</span><div class="avatar avatar--c" role="img" aria-label="Portrait of Renata"></div></article>
  <article class="card c1 r2"><svg class="stars" width="72" height="12"><use href="#stars"/></svg><p class="quote">Lorem ipsum dolor sit ipimetc onsectetur adipiscing</p><span class="author">Mark Ellis</span><div class="avatar" role="img" aria-label="Portrait of Mark Ellis"></div></article>
  <article class="card card--raised c2 r2"><svg class="stars" width="72" height="12"><use href="#stars"/></svg><p class="quote">Lorem ipsum dolor sit ipimetc onsectetur adipiscing</p><span class="author">Leo</span><div class="avatar avatar--b" role="img" aria-label="Portrait of Leo"></div></article>
  <article class="card c3 r2"><svg class="stars" width="72" height="12"><use href="#stars"/></svg><p class="quote">Lorem ipsum dolor sit ipimetc onsectetur adipiscing</p><span class="author">Renata</span><div class="avatar avatar--c" role="img" aria-label="Portrait of Renata"></div></article>
</section>

<!-- Home with request menu open -->
<section class="screen screen--menu">
  <div class="toolbar">
    <div class="btn btn--solid">Request feedback</div>
    <div class="btn btn--outline">Respond to Feedback</div>
  </div>
  <ul class="menu"><li>Adhoc Feedback</li><li>Mid Year Feedback</li><li>360 Feedback</li></ul>
  <article class="card c1 r1"><svg class="stars" width="72" height="12"><use href="#stars"/></svg><p class="quote">Lorem ipsum dolor sit ipimetc onsectetur adipiscing</p><span class="author">Mark Ellis</span><div class="avatar" role="img" aria-label="Portrait of Mark Ellis"></div></article>
  <article class="card card--raised c2 r1"><svg class="stars" width="72" height="12"><use href="#stars"/></svg><p class="quote">Lorem ipsum dolor sit ipimetc onsectetur adipiscing</p><span class="author">Leo</span><div class="avatar avatar--b" role="img" aria-label="Portrait of Leo"></div></article>
  <article class="card c3 r1"><svg class="stars" width="72" height="12"><use href="#stars"/></svg><p class="quote">Lorem ipsum dolor sit ipimetc onsectetur adipiscing</p><span class="author">Renata</span><div class="avatar avatar--c" role="img" aria-label="Portrait of Renata"></div></article>
  <article class="card c1 r2"><svg class="stars" width="72" height="12"><use href="#stars"/></svg><p class="quote">Lorem ipsum dolor sit ipimetc onsectetur adipiscing</p><span class="author">Mark Ellis</span><div class="avatar" role="img" aria-label="Portrait of Mark Ellis"></div></article>
  <article class="card card--raised c2 r2"><svg class="stars" width="72" height="12"><use href="#stars"/></svg><p class="quote">Lorem ipsum dolor sit ipimetc onsectetur adipiscing</p><span class="author">Leo</span><div class="avatar avatar--b" role="img" aria-label="Portrait of Leo"></div></article>
  <article class="card c3 r2"><svg class="stars" width="72" height="12"><use href="#stars"/></svg><p class="quote">Lorem ipsum dolor sit ipimetc onsectetur adipiscing</p><span class="author">Renata</span><div class="avatar avatar--c" role="img" aria-label="Portrait of Renata"></div></article>
</section>

<!-- Adhoc feedback -->
<section class="screen screen--adhoc">
  <h1 class="title">adhoc feedback</h1>
  <div class="divider"></div>
  <div class="search">Search
    <span class="go"><svg width="12" height="12" viewBox="0 0 12 12"><circle cx="5" cy="5" r="3.4" stroke="#fff" stroke-width="1.8" fill="none"/><path d="M7.6 7.6l2.8 2.8" stroke="#fff" stroke-width="1.8"/></svg></span>
  </div>

  <div class="row" style="top:174px"><div class="avatar" role="img" aria-label="Colleague portrait"></div><span class="name">Lorem Ipsum</span><div class="meta">01/09/23 &nbsp; 2.29AM<svg class="stars" width="72" height="12"><use href="#stars"/></svg></div><span class="action">Request feedback</span></div>
  <div class="row" style="top:271px"><div class="avatar avatar--b" role="img" aria-label="Colleague portrait"></div><span class="name">Lorem Ipsum</span><div class="meta">01/09/23 &nbsp; 2.29AM<svg class="stars" width="72" height="12"><use href="#stars"/></svg></div><span class="action">Request feedback</span></div>
  <div class="row row--open" style="top:368px"><div class="avatar avatar--b" role="img" aria-label="Colleague portrait"></div><span class="name">Lorem Ipsum</span><div class="meta">01/09/23 &nbsp; 2.29AM<svg class="stars" width="72" height="12"><use href="#stars"/></svg></div>
    <ul class="questions">
      <li><svg width="11" height="11"><use href="#tick"/></svg>Lorem ipsum dolor sit amet, consectetur adipiscing ?</li>
      <li><svg width="11" height="11"><use href="#tick"/></svg>Lorem ipsum dolor sit amet, consectetur adipiscing ?</li>
      <li><svg width="11" height="11"><use href="#tick"/></svg>Lorem ipsum dolor sit amet, consectetur adipiscing ?</li>
    </ul>
    <span class="action">Request feedback</span>
    <svg class="edit" width="14" height="14" viewBox="0 0 14 14"><path d="M2 12l.6-3L9.5 2.1l2.4 2.4L5 11.4z" fill="#888"/></svg>
  </div>
  <div class="row" style="top:508px"><div class="avatar" role="img" aria-label="Colleague portrait"></div><span class="name">Lorem Ipsum</span><div class="meta">01/09/23 &nbsp; 2.29AM<svg class="stars" width="72" height="12"><use href="#stars"/></svg></div><span class="action">Request feedback</span></div>
  <div class="row" style="top:607px"><div class="avatar avatar--c" role="img" aria-label="Colleague portrait"></div><span class="name">Lorem Ipsum</span><div class="meta">01/09/23 &nbsp; 2.29AM<svg class="stars" width="72" height="12"><use href="#stars"/></svg></div><span class="action">Request feedback</span></div>
</section>
</body>
</html>
```